Business card for Luxury Portable Restroom Trailer company

We are a Luxury Portable Restroom Trailer Company Called PELIKAR HIRES. Based in Orange County California. We provide portable restroom trailers for events, such as, Weddings, Concerts, Charity events, Sporting events, Tournaments, Corporate events, ect. We rent and Sell the Luxury restrooms. Our colors are white, grey, and Orange. As you will see in the logo we uploaded.
There are 2 people in the company so the names and titles will change for the 3 people but card will remain the same. Here is the information for each Person: Dennis Moyle CFO 555 018-3647
next Person: Wesley Tanford VP 555 018-3647
Next Person: Miles Tanford CEO 555 018-3647
Information to include on the card: Luxury Restroom Trailers Rental and Sales. Weddings, Concerts, Charity, Sporting and Corp. Events.

```html
<!DOCTYPE html>
<html lang="en">
<head>
<meta charset="utf-8">
<title>PELIKAR HIRES – Business Card</title>
<link rel="stylesheet" href="https://fonts.googleapis.com/css2?family=Montserrat:wght@400;700;800&display=swap">
<style>
  :root {
    --orange: #f26b24;
    --white: #ffffff;
    --backdrop: #a3a7a8;
  }
  * { margin: 0; padding: 0; box-sizing: border-box; }
  html, body {
    width: 1179px; height: 1200px; overflow: hidden;
    background: var(--backdrop);
    font-family: "Montserrat", Arial, sans-serif;
  }
  .card {
    position: absolute; left: 221px; width: 738px; height: 423px;
    background: var(--orange); color: var(--white); overflow: hidden;
  }
  .card--front { top: 161px; }
  .card--back { top: 619px; }

  .front__panel {
    position: absolute; left: 506px; top: 0; width: 232px; height: 100%;
    background: var(--white);
  }
  .front__badge {
    position: absolute; left: 370px; top: 52px; width: 328px; height: 328px;
    border-radius: 50%; background: var(--white);
    display: flex; flex-direction: column; align-items: center; justify-content: center;
    color: var(--orange); font-weight: 800; font-size: 40px; line-height: 1.1;
    letter-spacing: 1px;
  }

  .contacts { position: absolute; left: 35px; top: 90px; }
  .contact { margin-bottom: 12px; }
  .contact__name { font-weight: 700; font-size: 23px; text-transform: uppercase; line-height: 1.2; }
  .contact__title { font-weight: 400; font-size: 18px; line-height: 1.45; }
  .contact__phone { display: flex; align-items: center; gap: 8px; font-size: 18px; line-height: 1.45; }
  .contact__phone svg { width: 18px; height: 14px; fill: var(--white); }

  .back__name {
    position: absolute; left: 0; right: 0; top: 140px; text-align: center;
    font-weight: 800; font-size: 56px; letter-spacing: 2px; line-height: 1;
  }
  .services {
    position: absolute; left: 0; right: 0; top: 318px; text-align: center;
    font-size: 18px; line-height: 27px;
  }
  .services__item { white-space: nowrap; margin: 0 6px; }
  .services__item::before {
    content: ""; display: inline-block; width: 11px; height: 11px; border-radius: 50%;
    background: var(--white); margin-right: 8px; vertical-align: 1px;
  }
</style>
</head>
<body>
  <section class="card card--front">
    <div class="front__panel"></div>
    <div class="front__badge"><span>PELIKAR</span><span>HIRES</span></div>
    <div class="contacts">
      <div class="contact">
        <p class="contact__name">Dennis Moyle</p>
        <p class="contact__title">CFO</p>
        <p class="contact__phone"><svg viewBox="0 0 18 14" aria-hidden="true"><path d="M1 5C1 1 17 1 17 5L13 6 12 4H6L5 6ZM4 7H14L16 13H2Z"/></svg>555 018-3647</p>
      </div>
      <div class="contact">
        <p class="contact__name">Wesley Tanford</p>
        <p class="contact__title">VP</p>
        <p class="contact__phone"><svg viewBox="0 0 18 14" aria-hidden="true"><path d="M1 5C1 1 17 1 17 5L13 6 12 4H6L5 6ZM4 7H14L16 13H2Z"/></svg>555 018-3647</p>
      </div>
      <div class="contact">
        <p class="contact__name">Miles Tanford</p>
        <p class="contact__title">CEO</p>
        <p class="contact__phone"><svg viewBox="0 0 18 14" aria-hidden="true"><path d="M1 5C1 1 17 1 17 5L13 6 12 4H6L5 6ZM4 7H14L16 13H2Z"/></svg>555 018-3647</p>
      </div>
    </div>
  </section>

  <section class="card card--back">
    <h1 class="back__name">PELIKAR HIRES</h1>
    <div class="services">
      <p><span class="services__item">Luxury Restroom Trailers Rental and Sales</span></p>
      <p><span class="services__item">Weddings</span><span class="services__item">Concerts</span><span class="services__item">Charity</span><span class="services__item">Sporting and Corp</span><span class="services__item">Events</span></p>
    </div>
  </section>
</body>
</html>
```